New Design for Brightcoilheat [Zimpla]

Hello, This is my 2nd project here. I need a new web design for www.brightcoilheat.com.au which is one of my clients, and an extremely outdated website. It only has a few links and is fairly straight forward, looking for a more professional, up-to-date looking website. Please note: The website will be made under a zimpla white-label platform, so the design MUST be consistent with this type of platform. Many more projects will be up and coming so the best designers will definitely be selected for future projects.
Thankyou

• Please refer to www.brightcoilheat.com.au to find all the content.

```html
<!DOCTYPE html>
<html lang="en">
<head>
<meta charset="utf-8">
<title>Brightcoil Heat Pty Ltd</title>
<link href="https://fonts.googleapis.com/css2?family=Arimo:wght@400;700&family=Questrial&display=swap" rel="stylesheet">
<style>
:root{
  --navy:#0f3a78;
  --navy-dark:#0a2b5c;
  --navy-light:#1d5aa8;
  --heading:#123a72;
  --text:#1a1a1a;
  --muted:#8a8a8a;
  --footer:#e4e4e4;
  --frame:#d4d4d4;
  --tick:#3a9a2e;
  --brand-square:#1230e0;
}
*{margin:0;padding:0;box-sizing:border-box}
html,body{width:839px;height:1200px;overflow:hidden;background:#fff}
body{position:relative;font-family:"Arimo",Arial,sans-serif;color:var(--text)}
.site-header{position:absolute;left:0;top:0;width:839px;height:112px;
  background:linear-gradient(180deg,#0d3b7c 0%,#1a4f96 55%,#174a8c 100%)}
.brand{position:absolute;left:40px;top:20px;display:flex;align-items:center;gap:12px}
.brand-square{width:62px;height:62px;background:var(--brand-square)}
.brand-name{color:#fff;font-weight:700;font-size:16px;margin-top:-2px}
.main-nav{position:absolute;left:16px;top:102px;width:805px;height:43px;display:flex;
  background:linear-gradient(180deg,#1b4f95 0%,var(--navy) 50%,var(--navy-dark) 100%);border-radius:3px 3px 0 0}
.main-nav a{display:flex;align-items:center;justify-content:center;height:100%;color:#fff;text-decoration:none;
  font-family:"Questrial",sans-serif;font-size:13.5px;border-right:1px solid #0a2750;box-shadow:1px 0 0 #2a60a8}
.main-nav a.active{background:linear-gradient(180deg,#0c2f62,#0a2856)}
.hero{position:absolute;left:16px;top:145px;width:805px;height:288px;
  background:linear-gradient(180deg,#dde3ea 0%,#c7ccd3 40%,#7d848c 75%,#b59f86 100%)}
.section-title{font-family:"Questrial",sans-serif;color:var(--heading);font-size:18px;font-weight:400;letter-spacing:.2px}
.welcome{position:absolute;left:36px;top:460px;width:490px}
.welcome p{font-size:10.3px;line-height:18px;margin-top:11px}
.welcome p + p{margin-top:8px}
.products{position:absolute;left:36px;top:662px;width:490px}
.products ul{list-style:none;margin:10px 0 0 34px}
.products li{font-size:10.3px;line-height:16.7px}
.specialists{position:absolute;left:547px;top:460px;width:280px}
.specialists ul{list-style:none;margin-top:20px}
.specialists li{display:flex;align-items:center;height:25.2px;font-size:10.3px}
.specialists svg{margin:0 21px 0 6px;flex:none}
.gallery-item{position:absolute;top:918px;width:207px}
.gallery-frame{height:177px;border:1px solid var(--frame);padding:6px;background:#fff}
.gallery-photo{width:100%;height:100%}
.gallery-item figcaption{font-size:9.5px;text-align:center;margin-top:8px}
.site-footer{position:absolute;left:0;top:1130px;width:839px;height:70px;background:var(--footer);
  display:flex;align-items:center;justify-content:center;color:var(--muted);font-size:9.5px}
</style>
</head>
<body>
<header class="site-header">
  <div class="brand"><span class="brand-square"></span><span class="brand-name">Brightcoil Heat Pty Ltd</span></div>
</header>
<nav class="main-nav">
  <a class="active" href="#" style="width:118px">Home</a>
  <a href="#" style="width:108px">Products</a>
  <a href="#" style="width:110px">Services</a>
  <a href="#" style="width:109px">Blog</a>
  <a href="#" style="width:113px">Contact us</a>
</nav>
<div class="hero" role="img" aria-label="Photo of a large insulated industrial pressure vessel with flanged nozzles, strapped for transport, under a pale sky"></div>

<section class="welcome">
  <h1 class="section-title">Welcome to Brightcoil Heat Pty Ltd</h1>
  <p>Brightcoil Heat are one of Australia's leading suppliers and manufacturers of thermal fabrics and fabrications. The experience, knowledge and facility to design and fabricate gives you the quality Australian made products you demand.</p>
  <p>There are many variations of passages of Lorem Ipsum available, but the majority have suffered alteration in some form, by injected humour, or randomised words which don't look even slightly believable. If you are going to use a passage of Lorem Ipsum, you need to be sure there isn't anything embarrassing hidden in the middle of text. All the Lorem Ipsum generators on the Internet tend to repeat predefined chunks as necessary, making this the first true generator on the Internet.</p>
</section>

<section class="products">
  <h2 class="section-title">Thermal Product available at Brightcoil Heat</h2>
  <ul>
    <li>Ceramic Fibre Tapes, Ropes, Braids, Boards &amp; Insulation.</li>
    <li>Glass Fibre Tapes, Ropes, Braids, Boards &amp; Insulation.</li>
    <li>Furnace / Oven Tadpole Tape Seals.</li>
    <li>Boiler Tapes, Seals &amp; Gaskets.</li>
    <li>Boiler Close Up Kits.</li>
    <li>Welding Blankets, Curtains &amp; Screens</li>
    <li>Exhaust Thermal / Acoustic Covers.</li>
    <li>Thermal Hoods / Covers.</li>
    <li>Machine Thermal Covers.</li>
    <li>Thermal Fabrics.</li>
    <li>Thermal Fabrications - To your Specification</li>
    <li>Fabric / Metallic Expansion Joints &amp; Associated Metal Work</li>
  </ul>
</section>

<section class="specialists">
  <h2 class="section-title">Thermal and Sealing Specialists</h2>
  <ul>
    <li><svg width="14" height="14" viewBox="0 0 14 14"><rect x=".5" y=".5" width="13" height="13" fill="#fff" stroke="#8aa3c0"/><path d="M3 7l3 3 5-7" fill="none" stroke="var(--tick)" stroke-width="2.2"/></svg>Thermal Fabrics and Fabrications</li>
    <li><svg width="14" height="14" viewBox="0 0 14 14"><rect x=".5" y=".5" width="13" height="13" fill="#fff" stroke="#8aa3c0"/><path d="M3 7l3 3 5-7" fill="none" stroke="var(--tick)" stroke-width="2.2"/></svg>High and Low Temperature Insulation</li>
    <li><svg width="14" height="14" viewBox="0 0 14 14"><rect x=".5" y=".5" width="13" height="13" fill="#fff" stroke="#8aa3c0"/><path d="M3 7l3 3 5-7" fill="none" stroke="var(--tick)" stroke-width="2.2"/></svg>Furnace / Oven Door Seals</li>
    <li><svg width="14" height="14" viewBox="0 0 14 14"><rect x=".5" y=".5" width="13" height="13" fill="#fff" stroke="#8aa3c0"/><path d="M3 7l3 3 5-7" fill="none" stroke="var(--tick)" stroke-width="2.2"/></svg>Welding Blankets and Curtains</li>
    <li><svg width="14" height="14" viewBox="0 0 14 14"><rect x=".5" y=".5" width="13" height="13" fill="#fff" stroke="#8aa3c0"/><path d="M3 7l3 3 5-7" fill="none" stroke="var(--tick)" stroke-width="2.2"/></svg>Fabric Expansion Joints</li>
    <li><svg width="14" height="14" viewBox="0 0 14 14"><rect x=".5" y=".5" width="13" height="13" fill="#fff" stroke="#8aa3c0"/><path d="M3 7l3 3 5-7" fill="none" stroke="var(--tick)" stroke-width="2.2"/></svg>Boat Exhaust Covers</li>
    <li><svg width="14" height="14" viewBox="0 0 14 14"><rect x=".5" y=".5" width="13" height="13" fill="#fff" stroke="#8aa3c0"/><path d="M3 7l3 3 5-7" fill="none" stroke="var(--tick)" stroke-width="2.2"/></svg>Thermal Hoods / Covers</li>
    <li><svg width="14" height="14" viewBox="0 0 14 14"><rect x=".5" y=".5" width="13" height="13" fill="#fff" stroke="#8aa3c0"/><path d="M3 7l3 3 5-7" fill="none" stroke="var(--tick)" stroke-width="2.2"/></svg>Acoustic Materials</li>
    <li><svg width="14" height="14" viewBox="0 0 14 14"><rect x=".5" y=".5" width="13" height="13" fill="#fff" stroke="#8aa3c0"/><path d="M3 7l3 3 5-7" fill="none" stroke="var(--tick)" stroke-width="2.2"/></svg>Pump and Valve Packings</li>
    <li><svg width="14" height="14" viewBox="0 0 14 14"><rect x=".5" y=".5" width="13" height="13" fill="#fff" stroke="#8aa3c0"/><path d="M3 7l3 3 5-7" fill="none" stroke="var(--tick)" stroke-width="2.2"/></svg>Gasket Materials</li>
    <li><svg width="14" height="14" viewBox="0 0 14 14"><rect x=".5" y=".5" width="13" height="13" fill="#fff" stroke="#8aa3c0"/><path d="M3 7l3 3 5-7" fill="none" stroke="var(--tick)" stroke-width="2.2"/></svg>Standard and Non-Standard Gaskets</li>
    <li><svg width="14" height="14" viewBox="0 0 14 14"><rect x=".5" y=".5" width="13" height="13" fill="#fff" stroke="#8aa3c0"/><path d="M3 7l3 3 5-7" fill="none" stroke="var(--tick)" stroke-width="2.2"/></svg>Boilers Gaskets and Seals</li>
    <li><svg width="14" height="14" viewBox="0 0 14 14"><rect x=".5" y=".5" width="13" height="13" fill="#fff" stroke="#8aa3c0"/><path d="M3 7l3 3 5-7" fill="none" stroke="var(--tick)" stroke-width="2.2"/></svg>Spiral Wounds</li>
    <li><svg width="14" height="14" viewBox="0 0 14 14"><rect x=".5" y=".5" width="13" height="13" fill="#fff" stroke="#8aa3c0"/><path d="M3 7l3 3 5-7" fill="none" stroke="var(--tick)" stroke-width="2.2"/></svg>Brightcoil Seal</li>
    <li><svg width="14" height="14" viewBox="0 0 14 14"><rect x=".5" y=".5" width="13" height="13" fill="#fff" stroke="#8aa3c0"/><path d="M3 7l3 3 5-7" fill="none" stroke="var(--tick)" stroke-width="2.2"/></svg>and Lots more</li>
  </ul>
</section>

<figure class="gallery-item" style="left:44px">
  <div class="gallery-frame"><div class="gallery-photo" role="img" aria-label="Photo of a grey fabric expansion joint, type CR1, on a wooden pallet" style="background:linear-gradient(180deg,#3c3b40 0%,#6a6870 45%,#4d4b52 75%,#c8b99a 100%)"></div></div>
  <figcaption>Fabric Expansion Joint - Type CR1</figcaption>
</figure>
<figure class="gallery-item" style="left:317px">
  <div class="gallery-frame"><div class="gallery-photo" role="img" aria-label="Photo of a grey fabric expansion joint, type B1, bolted along a metal flange" style="background:linear-gradient(160deg,#2e2f36 0%,#8d8e9a 40%,#a7a8b3 65%,#3a3b42 100%)"></div></div>
  <figcaption>Fabric Expansion Joint - Type B1</figcaption>
</figure>
<figure class="gallery-item" style="left:589px">
  <div class="gallery-frame"><div class="gallery-photo" role="img" aria-label="Photo of white thermal insulation covers fitted to an engine exhaust system" style="background:linear-gradient(180deg,#2a2a2e 0%,#d9dadd 35%,#9ea4ab 65%,#2f3236 100%)"></div></div>
</figure>

<footer class="site-footer">2011 © Copyrights.Brightcoilheatpty.Received</footer>
</body>
</html>
```